Construction Company

Design a clutter free business card, it can be double-sided utilizing the logo for BDN Ltd simple with all relevant contact information.

Please also a letterhead design to function for the purposes of invoicing, all mail requirements, with header to be distinctive while the footer ties page together and incorporates all necessary information.

For now, please use generic / dummy text and when a winner is selected, I will disclose the contact information.

Hi Designers! Please read the updated brief which includes the design of a business card and letterhead. Thank you!

```html
<!DOCTYPE html>
<html lang="en">
<head>
<meta charset="utf-8">
<title>BDN Ltd Stationery</title>
<link rel="stylesheet" href="https://fonts.googleapis.com/css2?family=Montserrat:wght@400;700&family=Roboto:wght@400;500&display=swap">
<style>
  :root {
    --brand-blue: #2f4a9a;
    --brand-blue-dark: #263d82;
    --brand-gold: #c9a227;
    --ink: #3a3a3a;
    --ink-soft: #8a8a8a;
    --paper: #ffffff;
    --backdrop: #ececec;
  }
  * { box-sizing: border-box; margin: 0; padding: 0; }
  html, body { width: 1200px; height: 2406px; overflow: hidden; }
  body { background: var(--backdrop); font-family: "Roboto", Arial, sans-serif; color: var(--ink); position: relative; }

  .section { position: absolute; left: 0; width: 1200px; }
  .section--cards { top: 0; height: 800px; }
  .section--letter { top: 800px; height: 800px; background: #e6e6e6; }
  .section--envelopes { top: 1600px; height: 806px; }

  .wordmark { font-family: "Montserrat", Arial, sans-serif; font-weight: 700; color: var(--brand-blue); letter-spacing: 1px; white-space: nowrap; }
  .wordmark--light { color: var(--paper); }

  .card { position: absolute; box-shadow: 0 6px 14px rgba(0,0,0,.12); }
  .card--front { background: var(--paper); }
  .card--back { background: var(--brand-blue); display: flex; align-items: center; justify-content: center; }

  .card__logo { position: absolute; left: 8%; top: 30%; }
  .card__person { position: absolute; right: 10%; top: 12%; text-align: right; }
  .card__name { font-family: "Montserrat", Arial, sans-serif; font-weight: 700; color: var(--brand-blue); }
  .card__role { font-family: "Montserrat", Arial, sans-serif; font-weight: 700; color: var(--brand-gold); }
  .card__marker { position: absolute; right: 4%; top: 12%; background: var(--brand-blue); }
  .card__address { position: absolute; right: 10%; top: 52%; text-align: right; line-height: 1.3; }
  .card__contacts { position: absolute; left: 8%; bottom: 12%; line-height: 1.35; }

  .contact-line { display: flex; align-items: center; gap: 6px; }
  .contact-line svg { fill: var(--brand-blue); flex: none; }

  /* large pair */
  .card--lg { width: 500px; height: 286px; }
  .card--lg .card__logo { font-size: 40px; }
  .card--lg .card__name { font-size: 17px; }
  .card--lg .card__role { font-size: 13px; }
  .card--lg .card__marker { width: 9px; height: 22px; }
  .card--lg .card__address { font-size: 15px; }
  .card--lg .card__contacts { font-size: 15px; }
  .card--lg .contact-line svg { width: 12px; height: 12px; }
  .card--lg.card--back .wordmark { font-size: 52px; }

  /* small pair */
  .card--sm { width: 350px; height: 200px; }
  .card--sm .card__logo { font-size: 28px; }
  .card--sm .card__name { font-size: 12px; }
  .card--sm .card__role { font-size: 9px; }
  .card--sm .card__marker { width: 6px; height: 15px; }
  .card--sm .card__address { font-size: 10.5px; }
  .card--sm .card__contacts { font-size: 10.5px; }
  .card--sm .contact-line svg { width: 9px; height: 9px; }
  .card--sm.card--back .wordmark { font-size: 36px; }

  .letterhead { position: absolute; left: 110px; top: 50px; width: 495px; height: 700px; background: var(--paper); box-shadow: 0 6px 16px rgba(0,0,0,.12); padding: 48px 46px; font-size: 9px; }
  .letterhead__logo { font-size: 30px; }
  .letterhead__address { position: absolute; right: 46px; top: 110px; font-size: 10.5px; line-height: 1.35; color: var(--ink); }
  .letterhead__address .contact-line svg { width: 8px; height: 8px; }
  .letterhead__body { margin-top: 70px; width: 300px; color: var(--ink-soft); line-height: 1.5; }
  .letterhead__body p { margin-bottom: 10px; }
  .letterhead__sign { margin-top: 34px; width: 70px; border-bottom: 1px solid var(--ink); }

  .envelope { position: absolute; left: 150px; width: 900px; height: 330px; background: var(--paper); box-shadow: 0 6px 16px rgba(0,0,0,.12); overflow: hidden; }
  .envelope--back { top: 60px; }
  .envelope--front { top: 440px; }
  .envelope__flap { position: absolute; left: 0; top: 0; width: 900px; height: 120px; }
  .envelope__flap-logo { position: absolute; left: 0; top: 0; width: 900px; height: 110px; display: flex; align-items: center; justify-content: center; font-size: 40px; }
  .envelope__logo { position: absolute; left: 60px; top: 45px; font-size: 40px; }
  .envelope__address { position: absolute; left: 60px; bottom: 40px; font-size: 17px; line-height: 1.35; }
  .envelope__address .contact-line svg { width: 13px; height: 13px; }
</style>
</head>
<body>

<svg width="0" height="0" style="position:absolute">
  <defs>
    <symbol id="icon-phone" viewBox="0 0 16 16"><path d="M3 1h3l1.5 3.5-2 1.3a8 8 0 0 0 4.7 4.7l1.3-2L15 10v3a2 2 0 0 1-2 2A12 12 0 0 1 1 3a2 2 0 0 1 2-2z"/></symbol>
    <symbol id="icon-mail" viewBox="0 0 16 16"><path d="M1 3h14v10H1z M1 3l7 6 7-6" /></symbol>
    <symbol id="icon-web" viewBox="0 0 16 16"><circle cx="8" cy="8" r="7"/></symbol>
  </defs>
</svg>

<section class="section section--cards">
  <div class="card card--lg card--front" style="left:70px; top:257px;">
    <div class="card__logo wordmark">BDN Ltd</div>
    <span class="card__marker"></span>
    <div class="card__person">
      <div class="card__name">MARCUS HALE</div>
      <div class="card__role">Managing Director</div>
    </div>
    <div class="card__address">Alder Street,<br>Suite 12 Riverton</div>
    <div class="card__contacts">
      <div class="contact-line"><svg><use href="#icon-phone"/></svg>020.555.0148</div>
      <div class="contact-line"><svg><use href="#icon-mail"/></svg>office@northfieldmail.com</div>
      <div class="contact-line"><svg><use href="#icon-web"/></svg>www.northfieldmail.com</div>
    </div>
  </div>
  <div class="card card--lg card--back" style="left:630px; top:257px;">
    <div class="wordmark wordmark--light">BDN Ltd</div>
  </div>
</section>

<section class="section section--letter">
  <article class="letterhead">
    <div class="letterhead__logo wordmark">BDN Ltd</div>
    <div class="letterhead__address">
      Granite House, 14<br>Mill Lane, Leeds
      <div class="contact-line"><svg><use href="#icon-phone"/></svg>020.555.0148</div>
      <div class="contact-line"><svg><use href="#icon-mail"/></svg>info@bdnltd.com</div>
      <div class="contact-line"><svg><use href="#icon-web"/></svg>www.bdnltd.com</div>
    </div>
    <div class="letterhead__body">
      <p>Dear customer,</p>
      <p>Lorem ipsum dolor sit amet, consectetur adipisicing elit, sed do eiusmod tempor incididunt ut labore et dolore magna aliqua. Ut enim ad minim veniam, quis nostrud exercitation ullamco laboris nisi ut aliquip ex ea commodo consequat. Duis aute irure dolor in reprehenderit in voluptate velit esse cillum dolore eu fugiat nulla pariatur. Excepteur sint occaecat cupidatat non proident, sunt in culpa qui officia deserunt mollit anim id est laborum.</p>
      <p>Lorem ipsum dolor sit amet, consectetur adipisicing elit, sed do eiusmod tempor incididunt ut labore et dolore magna aliqua. Ut enim ad minim veniam, quis nostrud exercitation ullamco laboris nisi ut aliquip ex ea commodo consequat. Duis aute irure dolor in reprehenderit in voluptate velit esse cillum dolore eu fugiat nulla pariatur. Excepteur sint occaecat cupidatat non proident, sunt in culpa qui officia deserunt mollit anim id est laborum.</p>
      <p>Lorem ipsum dolor sit amet, consectetur adipisicing elit, sed do eiusmod tempor incididunt ut labore et dolore magna aliqua. Ut enim ad minim veniam, quis nostrud exercitation ullamco laboris nisi ut aliquip ex ea commodo consequat. Duis aute irure dolor in reprehenderit.</p>
      <p>Yours Sincerely,</p>
      <div class="letterhead__sign"></div>
    </div>
  </article>

  <div class="card card--sm card--front" style="left:700px; top:300px;">
    <div class="card__logo wordmark">BDN Ltd</div>
    <span class="card__marker"></span>
    <div class="card__person">
      <div class="card__name">MARCUS HALE</div>
      <div class="card__role">Managing Director</div>
    </div>
    <div class="card__address">Alder Street,<br>Suite 12 Riverton</div>
    <div class="card__contacts">
      <div class="contact-line"><svg><use href="#icon-phone"/></svg>020.555.0148</div>
      <div class="contact-line"><svg><use href="#icon-mail"/></svg>office@northfieldmail.com</div>
      <div class="contact-line"><svg><use href="#icon-web"/></svg>www.northfieldmail.com</div>
    </div>
  </div>
  <div class="card card--sm card--back" style="left:700px; top:530px;">
    <div class="wordmark wordmark--light">BDN Ltd</div>
  </div>
</section>

<section class="section section--envelopes">
  <div class="envelope envelope--back">
    <svg class="envelope__flap" viewBox="0 0 900 120" preserveAspectRatio="none">
      <path d="M0 0H900V70Q890 100 860 102L40 110Q5 108 0 80Z" fill="var(--brand-blue)"/>
    </svg>
    <div class="envelope__flap-logo wordmark wordmark--light">BDN Ltd</div>
  </div>

  <div class="envelope envelope--front">
    <div class="envelope__logo wordmark">BDN Ltd</div>
    <div class="envelope__address">
      Granite House, 14<br>Mill Lane, Leeds
      <div class="contact-line"><svg><use href="#icon-phone"/></svg>020.555.0148</div>
      <div class="contact-line"><svg><use href="#icon-mail"/></svg>info@bdnltd.com</div>
      <div class="contact-line"><svg><use href="#icon-web"/></svg>www.bdnltd.com</div>
    </div>
  </div>
</section>

</body>
</html>
```